Monthly Report PowerPoint Template

We are looking for a set of slides to use as a template for a report that we send out monthly on the state of the solar and storage market. It should be professional and low profile, attached are the slides we currently use/would like to replace: 1) title slide, 2) content summary, 3) content, and 4) section break. We are mainly concerned about a new design for 2), we are using the basic PowerPoint table and would like both a new table style and a version that is more visual. Thanks!

Requirements
Must have
• Light theme
Should not have
• No stock images

```html
<!DOCTYPE html>
<html lang="en">
<head>
<meta charset="utf-8">
<title>Volta Insight – Monthly Report Template</title>
<link href="https://fonts.googleapis.com/css2?family=Lato:wght@400;700;900&display=swap" rel="stylesheet">
<style>
:root{
  --navy:#13325f;
  --navy-deep:#0e2850;
  --gold:#f8b74a;
  --sky:#a9d1dc;
  --row-a:#d6eaf8;
  --row-b:#eaf4fc;
  --ink:#2b2f38;
  --muted:#6a6f78;
  --page:#ffffff;
}
*{margin:0;padding:0;box-sizing:border-box}
html,body{width:1050px;height:1200px;overflow:hidden;background:var(--page)}
body{font-family:'Lato',sans-serif;color:var(--ink);position:relative}
.slide{position:absolute;width:454px;height:256px;background:#fff;box-shadow:0 1px 4px rgba(0,0,0,.18);overflow:hidden}
.slide::before{content:"";position:absolute;left:0;top:0;bottom:0;width:7px;background:var(--gold);z-index:3}
.col-l{left:51px}.col-r{left:547px}
.row-1{top:41px}.row-2{top:328px}.row-3{top:615px}.row-4{top:903px}
.abs{position:absolute}
.brand{position:absolute;left:27px;top:22px;display:flex;align-items:center;gap:5px;font-size:18px;font-weight:400;color:var(--navy);z-index:2}
.brand-dot{width:15px;height:15px;border-radius:50%;background:var(--navy)}
.hi{color:var(--gold)}
.page-no{position:absolute;right:9px;bottom:9px;width:18px;height:18px;border-radius:50%;border:1.6px solid var(--navy);background:#dbeaf6;color:var(--navy);font-size:7px;font-weight:900;display:flex;align-items:center;justify-content:center}
.slide-title{position:absolute;left:0;right:0;top:18px;text-align:center;font-size:20px;font-weight:700;color:var(--navy)}
.cover-photo{position:absolute;inset:0;background:linear-gradient(100deg,#fff 0%,#f6f3ee 38%,#c9d3e2 60%,#6f86b8 80%,#33489a 100%)}
.cover-title{position:absolute;left:27px;top:70px;font-size:37px;font-weight:700;line-height:1.15;color:var(--navy);z-index:2}
.cover-sub{position:absolute;left:27px;top:168px;font-size:11.5px;color:var(--navy);z-index:2}
/* table */
.summary{position:absolute;left:27px;top:65px;width:411px;border-collapse:collapse;font-size:5.4px}
.summary th{background:var(--navy);color:#fff;text-align:left;font-weight:700;height:16px;padding-left:16px}
.summary td{height:16.5px;padding-left:16px;color:var(--navy)}
.summary td:first-child{font-weight:700}
.summary tr:nth-child(odd) td{background:var(--row-a)}
.summary tr:nth-child(even) td{background:var(--row-b)}
/* about */
.team-photo{position:absolute;left:23px;top:28px;width:199px;height:199px;border-radius:50%;background:radial-gradient(circle at 50% 35%,#c9b88d 0%,#8a8a6e 45%,#3d4a3a 100%)}
.about-title{position:absolute;left:254px;top:58px;font-size:19px;font-weight:700;color:var(--navy)}
.about-mission{position:absolute;left:253px;top:88px;width:180px;font-size:10.2px;font-weight:700;line-height:1.27;color:var(--gold)}
.about-body{position:absolute;left:253px;top:139px;width:185px;font-size:8.2px;line-height:1.45;color:var(--ink)}
/* section break */
.section-title{position:absolute;left:27px;top:92px;font-size:35px;font-weight:700;line-height:1.2;color:var(--navy)}
/* chart slide */
.chart-title{position:absolute;left:173px;top:20px;font-size:20px;font-weight:700;line-height:1.2;color:var(--navy)}
.chart-body{position:absolute;left:174px;top:75px;width:255px;font-size:7.9px;line-height:1.35;color:var(--ink)}
.bar-chart{position:absolute;left:0;top:0}
/* platform */
.platform-intro{position:absolute;left:90px;top:51px;width:274px;text-align:center;font-size:7.8px;line-height:1.35;color:var(--ink)}
.feature{position:absolute;top:100px;width:100px;height:116px;border:1.2px solid #e1e4ea;border-radius:5px;background:#fff;padding:16px 10px 0}
.feature.active{background:var(--navy);border-color:var(--navy);box-shadow:0 2px 6px rgba(0,0,0,.25)}
.feature-icon{width:26px;height:26px;border-radius:3px;background:#fdf1dc;display:flex;align-items:center;justify-content:center}
.feature.active .feature-icon{background:#fff}
.feature-name{margin-top:21px;padding-left:5px;border-left:1.2px solid var(--gold);font-size:7px;font-weight:700;color:var(--navy);line-height:1}
.feature.active .feature-name{color:#fff}
.feature-text{margin-top:9px;font-size:5.6px;line-height:1.6;color:var(--ink)}
.feature.active .feature-text{color:#fff}
/* pie */
.legend{position:absolute;width:112px;font-size:5.3px;line-height:1.55;color:var(--ink)}
.legend h4{font-size:8px;font-weight:400;color:#444;margin-bottom:4px;display:flex;align-items:center;gap:7px}
.legend.left{text-align:right}
.legend.left h4{justify-content:flex-end}
.legend .dot{width:7px;height:7px;border-radius:50%;display:inline-block}
/* closing */
.closing-photo{position:absolute;inset:0;background:linear-gradient(100deg,#fff 0%,#f5f2ec 35%,#cdd7e5 60%,#7d91be 82%,#3a4e9c 100%)}
.closing-title{position:absolute;left:31px;top:90px;font-size:36px;font-weight:700;color:var(--navy);z-index:2}
.closing-sub{position:absolute;left:31px;top:145px;font-size:11.5px;color:var(--navy);z-index:2}
.social{position:absolute;left:31px;top:168px;display:flex;gap:7px;z-index:2}
.social span{width:20px;height:20px;border-radius:50%;background:var(--navy)}
</style>
</head>
<body>

<!-- Title slide -->
<section class="slide col-l row-1">
  <div class="cover-photo" role="img" aria-label="City skyline behind rooftop solar panels, fading to white"></div>
  <div class="brand"><span class="brand-dot"></span>Volta Insight</div>
  <h1 class="cover-title">Volta Insight<br><span class="hi">June Update</span></h1>
  <p class="cover-sub">Residential and Commercial Solar</p>
</section>

<!-- Content summary -->
<section class="slide col-r row-1">
  <h2 class="slide-title">Report <span class="hi">Content Summary</span></h2>
  <table class="summary">
    <thead><tr><th style="width:125px">Section</th><th style="width:182px">Key Metrics / Topics Covered</th><th>Trend Summary</th></tr></thead>
    <tbody>
      <tr><td>Residential Permits</td><td>Monthly totals, YoY and MoM trends, top states</td><td>Growth in Sun Belt states</td></tr>
      <tr><td>Commercial &amp; Industrial Projects</td><td>New installs, pipeline changes, market segmentation</td><td>Decline in pipeline volume</td></tr>
      <tr><td>Energy Storage</td><td>Install capacity, state-level activity, incentives impact</td><td>Momentum in CA and NY</td></tr>
      <tr><td>Policy &amp; Regulation</td><td>Federal &amp; state updates, NEM, ITC developments</td><td>Legislative shifts ongoing</td></tr>
      <tr><td>Forecast &amp; Outlook</td><td>Install capacity, state-level activity, incentives impact</td><td>Momentum in CA and NY</td></tr>
      <tr><td>Technology Trends</td><td>Federal &amp; state updates, NEM, ITC developments</td><td>Legislative shifts ongoing</td></tr>
      <tr><td>Forecast &amp; Outlook</td><td>Install capacity, state-level activity, incentives impact</td><td>Momentum in CA and NY</td></tr>
      <tr><td>Policy &amp; Regulation</td><td>Federal &amp; state updates, NEM, ITC developments</td><td>Legislative shifts ongoing</td></tr>
    </tbody>
  </table>
  <span class="page-no">05</span>
</section>

<!-- About -->
<section class="slide col-l row-2">
  <div class="team-photo" role="img" aria-label="Team photo of five colleagues at a solar industry event"></div>
  <h2 class="about-title">About <span class="hi">Us</span></h2>
  <p class="about-mission">Our mission is to develop data and research solutions that support the expansion of clean energy.</p>
  <p class="about-body">Since 2018, Volta has provided real time data and research on the distributed energy transition. We are a dedicated and passionate team with expertise in solar, finance, and technology, driven by a commitment to clean energy development.</p>
  <span class="page-no">02</span>
</section>

<!-- Section break -->
<section class="slide col-r row-2">
  <div class="brand"><span class="brand-dot"></span>Volta Insight</div>
  <h2 class="section-title">Residential Solar:<br><span class="hi">Market Demand Trends</span></h2>
  <span class="page-no">06</span>
</section>

<!-- Bar chart -->
<section class="slide col-l row-3">
  <svg class="bar-chart" width="454" height="256" viewBox="0 0 454 256" font-family="Lato, sans-serif" text-anchor="middle">
    <g font-size="5.4" font-weight="700" fill="#13325f">
      <rect x="35" y="61" width="33" height="157" fill="#13325f"/><text x="51.5" y="57">95%</text>
      <rect x="75" y="86" width="33" height="132" fill="#a9d1dc"/><text x="91.5" y="82" font-weight="400" fill="#555">80%</text>
      <rect x="115" y="139" width="33" height="99" fill="#13325f" transform="translate(0,-20)"/><text x="131.5" y="115">60%</text>
      <rect x="155" y="144" width="33" height="74" fill="#a9d1dc"/><text x="171.5" y="140" font-weight="400" fill="#555">45%</text>
      <rect x="195" y="135" width="33" height="83" fill="#13325f"/><text x="211.5" y="131">50%</text>
      <rect x="235" y="152" width="33" height="66" fill="#a9d1dc"/><text x="251.5" y="148" font-weight="400" fill="#555">40%</text>
      <rect x="275" y="168" width="33" height="50" fill="#13325f"/><text x="291.5" y="164">30%</text>
      <rect x="315" y="201" width="33" height="17" fill="#a9d1dc"/><text x="331.5" y="197" font-weight="400" fill="#555">10%</text>
    </g>
    <g font-size="5.6">
      <text x="51.5" y="229" font-weight="700" fill="#13325f">Lorem<tspan x="51.5" dy="8">Ipsum</tspan></text>
      <text x="91.5" y="229" fill="#666">Finibus<tspan x="91.5" dy="8">Bonorum</tspan></text>
      <text x="131.5" y="229" font-weight="700" fill="#13325f">Nemo enim<tspan x="131.5" dy="8">ipsam</tspan></text>
      <text x="171.5" y="229" fill="#666">Sed ut<tspan x="171.5" dy="8">perspiciatis</tspan></text>
      <text x="211.5" y="229" font-weight="700" fill="#13325f">Ut enim ad<tspan x="211.5" dy="8">minima</tspan></text>
      <text x="251.5" y="229" fill="#666">Excepteur<tspan x="251.5" dy="8">sint</tspan></text>
      <text x="291.5" y="229" font-weight="700" fill="#13325f">Duis aute<tspan x="291.5" dy="8">irure</tspan></text>
      <text x="331.5" y="229" fill="#666">Ut enim ad<tspan x="331.5" dy="8">minim</tspan></text>
    </g>
  </svg>
  <h2 class="chart-title">Monthly Residential <span class="hi">Permits</span><br><span class="hi">Issued Trends</span></h2>
  <p class="chart-body">Lorem ipsum dolor sit amet, consectetur adipiscing elit, sed do eiusmod tempor incididunt ut labore et dolore magna aliqua. Ut enim ad minim veniam, quis nostrud exercitation ullamco laboris nisi ut aliquip ex ea commodo consequat.</p>
  <span class="page-no">03</span>
</section>

<!-- Platform overview -->
<section class="slide col-r row-3">
  <h2 class="slide-title">Platform <span class="hi">Overview</span></h2>
  <p class="platform-intro">Lorem ipsum dolor sit amet, consectetur adipiscing elit, sed do eiusmod tempor incididunt ut labore et dolore magna aliqua. Ut enim ad minim veniam, quis nostrud exercitation ex ea commodo consequat.</p>
  <div class="feature" style="left:16px">
    <div class="feature-icon"><svg width="16" height="18" viewBox="0 0 16 18" fill="none" stroke="#f8b74a" stroke-width="1"><rect x="1" y="1" width="14" height="16" rx="1"/><circle cx="6" cy="7" r="3"/><path d="M4 14h8M9 11v3M11 9v5M13 12v2"/></svg></div>
    <div class="feature-name">Research Reports</div>
    <p class="feature-text">Monitor industry trends, our forecast, and manufacturer market share.</p>
  </div>
  <div class="feature" style="left:126px">
    <div class="feature-icon"><svg width="18" height="16" viewBox="0 0 18 16" fill="none" stroke="#f8b74a" stroke-width="1"><path d="M9 1v13M4 15h10M2 4h14M2 4l-2 5h4zM16 4l-2 5h4z"/></svg></div>
    <div class="feature-name">Policy Tracking</div>
    <p class="feature-text">Stay up to date on policies across the U.S. that will impact the industry.</p>
  </div>
  <div class="feature active" style="left:236px">
    <div class="feature-icon"><svg width="18" height="16" viewBox="0 0 18 16" fill="none" stroke="#f8b74a" stroke-width="1"><rect x="1" y="1" width="16" height="11" rx="1"/><path d="M6 15h6M9 12v3M4 9l3-3 3 2 4-4"/></svg></div>
    <div class="feature-name">Data Platform</div>
    <p class="feature-text">Visualize data from thousands of sources aggregated in real time.</p>
  </div>
  <div class="feature" style="left:346px">
    <div class="feature-icon"><svg width="18" height="16" viewBox="0 0 18 16" fill="none" stroke="#f8b74a" stroke-width="1"><rect x="1" y="1" width="16" height="8" rx="1"/><path d="M4 7V5M7 7V3M10 7V4M13 7V2"/><circle cx="4" cy="12" r="1.6"/><circle cx="9" cy="12" r="1.6"/><circle cx="14" cy="12" r="1.6"/></svg></div>
    <div class="feature-name">Analytics Support</div>
    <p class="feature-text">Gain access to our team of data and policy analysts.</p>
  </div>
  <span class="page-no">07</span>
</section>

<!-- Pie chart -->
<section class="slide col-l row-4">
  <h2 class="slide-title">Monthly Residential <span class="hi">Permits</span><br><span class="hi">Issued Trends</span></h2>
  <svg class="abs" style="left:153px;top:95px" width="150" height="130" viewBox="-75 -60 150 130">
    <ellipse cx="0" cy="12" rx="72" ry="55" fill="#0d2449"/>
    <rect x="-72" y="0" width="144" height="12" fill="#0d2449"/>
    <path d="M0 0L0 -55A72 55 0 0 1 69.5 14.2Z" fill="#174f94"/>
    <path d="M0 0L69.5 14.2A72 55 0 0 1 -12.5 54.2Z" fill="#15376c"/>
    <path d="M0 0L-12.5 54.2A72 55 0 0 1 -67.7 18.8Z" fill="#102d5a"/>
    <path d="M0 0L-67.7 18.8A72 55 0 0 1 -59 -31.5Z" fill="#1e6cc9"/>
    <path d="M0 0L-59 -31.5A72 55 0 0 1 0 -55Z" fill="#1b5fb3"/>
  </svg>
  <div class="legend left" style="left:30px;top:94px">
    <h4>Volta Insight 1 <span class="dot" style="background:#13325f"></span></h4>
    Duis aute irure dolor in reprehenderit in voluptate velit esse cillum dolore eu fugiat nulla pariatur.
  </div>
  <div class="legend left" style="left:30px;top:141px">
    <h4>Volta Insight 2 <span class="dot" style="background:#1e6cc9"></span></h4>
    Duis aute irure dolor in reprehenderit in voluptate velit esse cillum dolore eu fugiat nulla pariatur.
  </div>
  <div class="legend left" style="left:30px;top:188px">
    <h4>Volta Insight 3 <span class="dot" style="background:#15376c"></span></h4>
    Duis aute irure dolor in reprehenderit in voluptate velit esse cillum dolore eu fugiat nulla pariatur.
  </div>
  <div class="legend" style="left:307px;top:94px">
    <h4><span class="dot" style="background:#1e7fd6"></span> Volta Insight 4</h4>
    <div style="padding-left:14px">Duis aute irure dolor in reprehenderit in voluptate velit esse cillum dolore eu fugiat nulla pariatur.</div>
  </div>
  <div class="legend" style="left:307px;top:141px">
    <h4><span class="dot" style="background:#13325f"></span> Volta Insight 5</h4>
    <div style="padding-left:14px">Duis aute irure dolor in reprehenderit in voluptate velit esse cillum dolore eu fugiat nulla pariatur.</div>
  </div>
  <div class="legend" style="left:307px;top:188px">
    <h4><span class="dot" style="background:#1b5fb3"></span> Volta Insight 6</h4>
    <div style="padding-left:14px">Duis aute irure dolor in reprehenderit in voluptate velit esse cillum dolore eu fugiat nulla pariatur.</div>
  </div>
  <span class="page-no">04</span>
</section>

<!-- Closing -->
<section class="slide col-r row-4">
  <div class="closing-photo" role="img" aria-label="City skyline behind rooftop solar panels, fading to white"></div>
  <div class="brand"><span class="brand-dot"></span>Volta Insight</div>
  <h2 class="closing-title">Thank <span class="hi">You</span></h2>
  <p class="closing-sub">Residential and Commercial Solar</p>
  <div class="social" aria-label="Social media links"><span></span><span></span></div>
</section>

</body>
</html>
```